The Merry Hound - Dog Training Business Card Design

I need a business card design for a new dog training company based in Cronulla NSW called The Merry Hound. I run puppy pre school classes, adult dog classes and do one on one training in the person's home.
I have studied for 2 years and use positive reinforcement training methods based on how dogs learn. I believe in communicating with our dogs what we want them to do rather than punish them for behaviours we don't like. I would like to see designs that use the colours that are used in my logo (please see attached)
I would like a simple and classic looking design. I don't want cartoon images of dogs or any animal images or drawings on the card. I have created my logo with this mindset. I am open to the subtle use of a dog's tail, paws or paw print.

Target Market(s)

high end area which is why I want a classic looking design
adults aged 25 and over

Industry/Entity Type

Dog Training

Contact Information for Business Card

Miriam Caslett
ORBIS Trained Professional Dog Trainer
www.themerryhound-example.com.au
0499731628
miriam@themerryhound-example.com.au

Font styles to use
Sans Serif

Colors
ffffff
86cae6
757575

Requirements
Must have
• Logo - I am trying to attach my logo and colour palette but it won't allow me. I will contact the company and upload ASAP.
Should not have
• images of dogs or cartoon drawings

```html
<!DOCTYPE html>
<html lang="en">
<head>
<meta charset="utf-8">
<title>The Merry Hound – Business Cards</title>
<link href="https://fonts.googleapis.com/css2?family=Questrial&family=Montserrat:wght@700&display=swap" rel="stylesheet">
<style>
  :root {
    --backdrop: #2f2f31;
    --sky: #86cae6;
    --sky-card-top: #c4e0f1;
    --sky-card-bottom: #a9cde6;
    --slate: #757575;
    --slate-soft: #9a9a9a;
    --paper: #ffffff;
    --paper-shade: #eeeeee;
    --band: rgba(0, 0, 0, 0.035);
    --ink: #1e1e1e;
    --icon: #8fb3d3;
  }
  * { box-sizing: border-box; margin: 0; padding: 0; }
  html, body { width: 1200px; height: 900px; overflow: hidden; }
  body {
    background: var(--backdrop);
    font-family: "Questrial", "Century Gothic", sans-serif;
    position: relative;
  }

  /* Front card */
  .card-front {
    position: absolute;
    left: 60px; top: 290px;
    width: 560px; height: 320px;
    border-radius: 30px;
    background: linear-gradient(160deg, var(--sky-card-top), var(--sky-card-bottom));
    display: flex; flex-direction: column;
    align-items: center; justify-content: center;
    gap: 14px;
  }
  .front-brand {
    display: flex; align-items: center; gap: 16px;
  }
  .front-brand__name {
    font-size: 54px;
    color: var(--paper);
    letter-spacing: 1px;
  }
  .front-brand__dot {
    width: 30px; height: 30px; border-radius: 50%;
    background: var(--slate);
  }
  .front-tagline {
    font-size: 21px;
    letter-spacing: 4px;
    color: var(--paper);
    opacity: 0.85;
    text-transform: uppercase;
  }

  /* Back card */
  .card-back {
    position: absolute;
    left: 700px; top: 170px;
    width: 380px; height: 560px;
    border-radius: 36px;
    background: linear-gradient(180deg, var(--paper) 0%, var(--paper) 55%, var(--paper-shade) 100%);
    overflow: hidden;
  }
  .trainer {
    text-align: center;
    padding-top: 44px;
  }
  .trainer__name {
    font-family: "Montserrat", "Century Gothic", sans-serif;
    font-weight: 700;
    font-size: 22px;
    color: var(--sky);
    letter-spacing: 0.5px;
  }
  .trainer__role {
    font-size: 15px;
    color: var(--ink);
    line-height: 1.3;
    margin-top: 4px;
  }
  .back-brand {
    margin-top: 64px;
    display: flex; align-items: center; justify-content: center; gap: 12px;
  }
  .back-brand__name {
    font-size: 34px;
    color: var(--slate-soft);
  }
  .back-brand__dot {
    width: 24px; height: 24px; border-radius: 50%;
    background: var(--sky);
  }
  .contacts {
    position: absolute;
    left: 0; right: 0; bottom: 42px;
    list-style: none;
  }
  .contact {
    display: flex; align-items: center; gap: 16px;
    height: 58px;
    padding-left: 26px;
    font-size: 14.5px;
    color: var(--ink);
    border-top: 1px solid rgba(0,0,0,0.04);
  }
  .contact:nth-child(odd) { background: var(--band); }
  .contact svg { width: 30px; height: 30px; flex: none; }
</style>
</head>
<body>

  <section class="card-front" aria-label="Business card front">
    <div class="front-brand">
      <span class="front-brand__name">The Merry Hound</span>
      <span class="front-brand__dot"></span>
    </div>
    <p class="front-tagline">Positive Training Specialist</p>
  </section>

  <section class="card-back" aria-label="Business card back">
    <header class="trainer">
      <h1 class="trainer__name">Miriam Caslett</h1>
      <p class="trainer__role">ORBIS Trained<br>Professional Dog Trainer</p>
    </header>

    <div class="back-brand">
      <span class="back-brand__name">The Merry Hound</span>
      <span class="back-brand__dot"></span>
    </div>

    <ul class="contacts">
      <li class="contact">
        <svg viewBox="0 0 30 30" aria-hidden="true">
          <rect x="8" y="2" width="14" height="26" rx="2.5" fill="none" stroke="var(--icon)" stroke-width="2"/>
          <line x1="8" y1="6" x2="22" y2="6" stroke="var(--icon)" stroke-width="1.5"/>
          <line x1="8" y1="23" x2="22" y2="23" stroke="var(--icon)" stroke-width="1.5"/>
          <circle cx="15" cy="25.5" r="1.2" fill="var(--icon)"/>
        </svg>
        <span>0499731628</span>
      </li>
      <li class="contact">
        <svg viewBox="0 0 30 30" aria-hidden="true">
          <rect x="2" y="7" width="26" height="17" fill="var(--icon)"/>
          <polyline points="2,7 15,17 28,7" fill="none" stroke="var(--paper)" stroke-width="1.6"/>
          <line x1="2" y1="24" x2="12" y2="15" stroke="var(--paper)" stroke-width="1.2"/>
          <line x1="28" y1="24" x2="18" y2="15" stroke="var(--paper)" stroke-width="1.2"/>
        </svg>
        <span>miriam@themerryhound-example.com.au</span>
      </li>
      <li class="contact">
        <svg viewBox="0 0 30 30" aria-hidden="true">
          <circle cx="15" cy="15" r="12" fill="none" stroke="var(--icon)" stroke-width="2"/>
          <ellipse cx="15" cy="15" rx="5" ry="12" fill="none" stroke="var(--icon)" stroke-width="1.5"/>
          <line x1="3" y1="15" x2="27" y2="15" stroke="var(--icon)" stroke-width="1.5"/>
        </svg>
        <span>www.themerryhound-example.com.au</span>
      </li>
    </ul>
  </section>

</body>
</html>
```